Tavington Inc 1 pg brochure for entrepreneurs

We need a one page brochure (2 sided) designed for a finance and strategy consulting company called Tavington Inc. which does work in Canada and the United States currently. This company works with entrepreneurs, helping them to establish finance operations, evaluate their financial infomation and apply insight from it to business strategies. Essentially we help entrepreneurs grow their business ... we take care of their finance needs and give them sound business advice ... allowing them to focus on their core business and business strategy.

This one page brochure is meant to caputure what services we provide but also positon that we are also entrepreneurs and we understand how entrepreneurs think .... we not only bring technical competence but cultural insight in this regard as well. We understand how nimble and stealth an entrepreneur's business is so we don't gouge them with expensive consulting fees. We don't want to look like a massive corporation ...we want to look professional, smart and reliable. We want to reflect that we are entrepreneural ourselves even in fact that we have a niche offering that is totally targeted to businesses of this nature.

Major emphasis points for the piece are
1) our core values, this could be a side bar or box
2) the credentials of our founder, he is technically competent and an entrepreneur himself (we have his picture to include)
3) our offerings, what we can do for a company, the client quotes provided are a good illustration of what we offer, the relief we provide a client and of what value we provide - make sure you read these, this could also be a side bar or box, some kind of special call out so the service offerings are very clear

The brochure needs to be editable, so in a format that we can work with it for future, if we need to make updates, one that we can use in Microsoft word and convert to a PDF format. It will be emailed to people (in pdf) and also brought to meetings.

We have a new logo and this design should be an extenstion of it from a colour, look and feel perspective. The piece should also be clean and not too copy heavy so we encourage use of sub-heads, whitespace, etc.

When we send this piece out or hand it to someone, the impression should be "I am comfortable with Tavington Inc. they can help me and are people who get me, people I can trust to work closely with me on my business who are personally vested in my success".
Updates

Hello all, thank you for sumitting designs, there is some great work here.  A few changes/requests ...

Pls add the following headline on the front page right off the top

Entrepreneurs helping entrepreneurs, providing strategic financial services

Can we put Services on the front page? and call them out with treatment in a text box or with something strong that creates emphasis

Can the quote pls be broken up as opposed to one long list of 6 quotes? They can be floated throughout the piece, we can use less of them (or not) and put them on the front and back of the brochure? 

Also looking for the final product to be a little more bold in colour ...

Thx all, let us know if you have questions

Target Market(s)

Individuals (CEO) who runs their own established, yet growing business, who needs a business-minded CFO

Industry/Entity Type

Financial

Requirements
Must have
• Must have photo of founder, include his name and credentials under photo
All copy provide must be included
If not sure of a headline put in dummy text and we will provide headline or sub head copy
Should not have
• Fonts to be clean, no serif fonts. Should compliment logo, not the same font exactly but easily replicable in Microsoft Word and complimentary
No illustrations or cliche clip art

```html
<!DOCTYPE html>
<html lang="en">
<head>
<meta charset="utf-8">
<title>Tavington Inc – Brochure</title>
<link rel="stylesheet" href="https://fonts.googleapis.com/css2?family=Arimo:ital,wght@0,400;0,700;1,400&display=swap">
<style>
  :root {
    --navy: #1b1a6b;
    --ink: #4a4234;
    --muted: #6b6357;
    --quote: #7a7368;
    --rule: #8a8aa8;
    --page: #ffffff;
    --canvas: #ffffff;
    --brand-blue: #2a3f8f;
  }
  * { box-sizing: border-box; margin: 0; padding: 0; }
  html, body { width: 1200px; height: 1042px; overflow: hidden; background: var(--canvas); }
  body { position: relative; font-family: "Arimo", Arial, sans-serif; color: var(--ink); }

  .page {
    position: absolute; top: 136px; width: 540px; height: 762px;
    background: var(--page);
    box-shadow: 0 3px 8px rgba(0,0,0,.28);
  }
  .page--front { left: 42px; }
  .page--back { left: 618px; }

  .hero { position: absolute; left: 0; top: 0; width: 540px; height: 212px; }
  .hero--front { background: linear-gradient(100deg, #c9c3b8 0%, #e8e2d6 30%, #d7d9df 55%, #b9b3aa 100%); }
  .hero--back { background: linear-gradient(95deg, #e9e3d6 0%, #c7c0b4 30%, #eceae4 60%, #c9c2b7 85%, #e4e4e2 100%); }

  .brand-tag {
    position: absolute; right: 0; top: 158px; width: 132px; height: 42px;
    background: #fff; display: flex; align-items: center; gap: 7px; padding-left: 10px;
  }
  .brand-tag__square { width: 22px; height: 22px; background: var(--brand-blue); flex: none; }
  .brand-tag__name { font-size: 13px; font-weight: 400; color: var(--brand-blue); white-space: nowrap; }

  .headline {
    position: absolute; left: 38px; top: 236px;
    font-size: 20.5px; font-weight: 700; color: var(--navy); letter-spacing: .1px;
  }
  .intro {
    position: absolute; left: 38px; top: 269px; width: 470px;
    font-size: 9px; line-height: 13.2px;
  }

  .founder { position: absolute; left: 32px; top: 357px; width: 110px; }
  .founder__photo {
    width: 103px; height: 150px; border: 1px solid #b9b9c9; padding: 4px; background: #fff;
  }
  .founder__photo div { width: 100%; height: 100%; background: linear-gradient(180deg, #5a5a5a 0%, #3d3d3f 55%, #242427 100%); }
  .founder__caption { margin-top: 8px; font-size: 7.3px; text-align: center; width: 103px; color: var(--ink); }

  .section-title { font-size: 12.5px; font-weight: 700; color: var(--navy); letter-spacing: .3px; }
  .who__title { position: absolute; left: 170px; top: 363px; }
  .who__col { position: absolute; top: 386px; font-size: 9px; line-height: 13.2px; text-align: justify; }
  .who__col p + p { margin-top: 13px; }
  .who__col--a { left: 170px; width: 152px; letter-spacing: .35px; }
  .who__col--b { left: 345px; width: 160px; }

  .footer {
    position: absolute; left: 0; right: 0; top: 740px;
    font-size: 7px; text-align: center; color: #333;
  }

  .services-title { position: absolute; left: 24px; top: 240px; }
  .values-title { position: absolute; left: 24px; top: 468px; }
  .bullets { position: absolute; left: 24px; width: 276px; list-style: none; font-size: 9px; line-height: 13.4px; }
  .bullets li { position: relative; padding-left: 14px; margin-bottom: 7px; }
  .bullets li::before { content: ""; position: absolute; left: 1px; top: 5px; width: 4px; height: 4px; border-radius: 50%; background: var(--ink); }
  .bullets--services { top: 264px; }
  .bullets--values { top: 492px; }

  .divider { position: absolute; left: 318px; top: 226px; width: 1px; height: 462px; background: var(--rule); }

  .voices { position: absolute; left: 330px; top: 232px; width: 190px; }
  .voices__title { font-size: 8.7px; font-weight: 700; color: #333; line-height: 11.5px; }
  .voices__quote { font-size: 8.7px; font-style: italic; color: var(--quote); line-height: 11.5px; padding-bottom: 9px; border-bottom: 1px solid #c9c9d4; margin-top: 13px; }
  .voices__quote:last-child { border-bottom: 0; }
</style>
</head>
<body>

<section class="page page--front">
  <div class="hero hero--front" role="img" aria-label="Photo of business colleagues talking together in a bright meeting lounge"></div>
  <div class="brand-tag"><span class="brand-tag__square"></span><span class="brand-tag__name">Tavington Inc</span></div>

  <h1 class="headline">ENGAGING PEOPLE. BUILDING BUSINESS.</h1>
  <p class="intro">Tavington Inc. provides strategic financial services to entrepreneurs. We are entrepreneurs assisting entrepreneurs. By engaging us, entrepreneurs can regularly access senior executive financial acumen and strategic discipline without having to hire a full-time financial executive or overspend on third-party service providers who are transactional in nature.</p>

  <figure class="founder">
    <div class="founder__photo"><div role="img" aria-label="Portrait photo of the founder in a dark suit"></div></div>
    <figcaption class="founder__caption">Martin Castellane - Founder</figcaption>
  </figure>

  <h2 class="section-title who__title">WHO ARE WE?</h2>
  <div class="who__col who__col--a">
    <p>Tavington Inc. evolved out of the companies, partnerships and relationships that Martin Castellane, its founder, has nurtured and built over the last 22 years. Mr Castellane, the founder of Tavington, is an entrepreneur himself having built his own companies and managed several successful investment funds whose mandates were to invest in entrepreneurial growth companies.</p>
    <p>Over his career, he has worked extensively with entrepreneurs like himself who have struggled to build an experienced and engaged executive management team.</p>
    <p>Mr Castellane has a proven track record of developing and implementing strategic corporate policy. His experience and education is in corporate finance, portfolio management and building businesses. He is a registered</p>
  </div>
  <div class="who__col who__col--b">
    <p>Portfolio Manager, has earned an MBA from the Lakeshore University (1995) and is a Chartered Financial Analyst (CFA, 1999). He applies this competence to evaluating an entrepreneur's vision and corporate strategies and assisting in translating them into higher growth, improved efficiency and higher profitability. Mr Castellane has extensive experience in public and private, debt and equity capital markets, involving raising, managing and investing capital and completing corporate transactions. He has evaluated hundreds of corporate business strategies for potential investment.</p>
    <p>Other core skills include financial and tax analysis, working with high-performing investment teams, managing financial and accounting functions, designing and implementing operational and compliance systems.</p>
  </div>

  <p class="footer">Tavington Inc. &nbsp;1180 Ridgeview Avenue NW, Calgary Alberta, Canada, T3A 4K2 403.555.0142 | Email: martinc@tavingtoninc.ca</p>
</section>

<section class="page page--back">
  <div class="hero hero--back" role="img" aria-label="Photo of a smiling team around a laptop with two people shaking hands"></div>
  <div class="brand-tag"><span class="brand-tag__square"></span><span class="brand-tag__name">Tavington Inc</span></div>

  <h2 class="section-title services-title">OUR SERVICES</h2>
  <ul class="bullets bullets--services">
    <li>We work intimately with our clients to determine their corporate and personal objectives.</li>
    <li>We evaluate corporate strategies and assist in aligning them with financial ones.</li>
    <li>We assist in budgeting, investing, financial forecasting and analysis and asset management.</li>
    <li>We develop and implement accountability financial systems, processes and reporting.</li>
    <li>We manage capital raising efforts, tax structuring issues and corporate transactions including mergers, acquisitions, and the sale of your business.</li>
  </ul>

  <h2 class="section-title values-title">CORE VALUES</h2>
  <ul class="bullets bullets--values">
    <li>We love working with entrepreneurs because they like adventure.</li>
    <li>We understand the high energy, creativity and passion required to take high risks and achieve a corporate vision.</li>
    <li>We like entrepreneurs because they are focused on achievement. They are “can-do” people who take action.</li>
    <li>We like entrepreneurs because their business relationships are like family. Entrepreneurs are personally invested and value personal relationships with amazing people.</li>
    <li>We like entrepreneurs because they work hard and live well. Health and wellness is as important as financial success, and most of all having fun is central to the mind set of most successful entrepreneurs.</li>
  </ul>

  <div class="divider"></div>

  <aside class="voices">
    <p class="voices__title">Common comments from visionary entrepreneurs (which Tavington Inc. helps address) include:</p>
    <p class="voices__quote">“I need a financial executive to integrate my operating objectives with my financial ones. They are not aligned and are working against each other”</p>
    <p class="voices__quote">“If I could hire a right-hand who I trust intimately to help me with financial matters, I could free up more time to run the business or work on strategy”</p>
    <p class="voices__quote">“I need a financial executive who gets the numbers, can think strategically and translate that combined expertise and understanding into forward-looking corporate strategies”</p>
    <p class="voices__quote">“I need a financial executive who understands the inherent makeup of an entrepreneur”</p>
    <p class="voices__quote">“I would be a billionaire if I could implement better financial systems and apply strategic discipline.”</p>
    <p class="voices__quote">“If I could hire my equal in a financial capacity, my executive team would be complete”</p>
  </aside>

  <p class="footer">Tavington Inc. &nbsp;1180 Ridgeview Avenue NW, Calgary Alberta, Canada, T3A 4K2 403.555.0142 | Email: martinc@tavingtoninc.ca</p>
</section>

</body>
</html>
```